Affiliate website design and wireframe

We need a design of an affiliate website for an application we purchased, it is important that you build the website pages according to the developer of the applications specifications (please see attached documents) the developer of the application will configure the pages and add them to the site. Please take special note of his comments below.

We all so need you to create a wire frame so the developer can test everything (http://sketchwire.tolvaro.vn/)

It will be the homepage and about 16 inner pages (please see attached files)
Here is our website http://bluvendmarket.com/affiliate/affiliates/index.php

The version of the software we purchased is the Kivo Partner Hubline version

Comments from the developers

1. I will need the source files of the design (photoshop .psd files and font files if custom fonts are used), since the implementation is closely bound to component sizes (like border width, margin width etc.) and colors. If you own a corporate design manual, it's crucial to send it as well. Also, please, make sure if you use custom fonts, that these allow legal website integration (like google web fonts).

2. Any and every content is controlled via templates. All editing/adding/removing etc. is done here. The template files are essentially html/php documents, they use a template engine called quillo (http://www.quillo.net/) which has it's own language similar to php.

3. .psd files are ideal, because we deal with the specifics of KPX/KPH implementation on a daily basis. Any html/css developed in advance may prove to be a poor choice. You may choose to let an in-house developer do the job, but experience wise this is more costly, since he will not be accustomed to the template/functionality systems of KPX/KPH.

4. I will need the source files of the design (photoshop .psd files and font files if custom fonts are used), since the implementation is closely bound to component sizes (like border width, margin width etc.) and colors. If you own a corporate design manual, it's crucial to send it as well. Also, please, make sure if you use custom fonts, that these allow legal website integration (like google web fonts).

Regards,

Dorek Hanval
Multimedia Design

We prefer illustrations more than pictures of real people.

This is the home page, it is asking for Merchant and Affiliate sign up, not just affiliate.

http://bluvendmarket.com/affiliate/index.php

Please note the home page features both Merchant and Affiliate sign up

We are looking for illustration design not just stock images

Please remember the search menu that searches for the available programs, see the example we gave you, look at the search menu at the top of the page http://www.tradelumo.com/

We are reviewing everything, no need to send more designs

Target Market(s)

Natural Products Manufacturers
Natural products Sales reps
Natural Products Bloggers
Social Marketing

Industry/Entity Type

Software

Requirements
Must have
• 1. All links on pages should go to the appropriate pages.
2. Colors can be based on our logo design (look at the attachments)
3. Here is our website http://bluvendmarket.com/affiliate/affiliates/index.php
4. We have attached a drawing of how we think the homepage concept should follow.
5. Main concept of design, is trying to show our sales people (Affiliates) are doing multiple things to advertise and sell the merchants products.(see logo)
6. Need to be able to edit all text and images.
7. Our target audience is Natural product sales people (Advertisers, bloggers, ext) and natural product manufacturers.
8. You can speak to the company who made the application, through live chat, on there website http://www.kivopartnerhubline.com/
Nice to have
• See Attached Documents.
site should take up whole website pages
Look For fun Illustrated Website, one of the better ones we have seen is http://www.tradelumo.com/index.cfm
Should not have
• Please look very carefully at developers comment above.

```html
<!DOCTYPE html>
<html lang="en">
<head>
<meta charset="utf-8">
<title>Bluvend Market – Affiliate Network</title>
<link rel="stylesheet" href="https://fonts.googleapis.com/css2?family=Roboto:ital,wght@0,300;0,400;0,500;0,700;1,400&display=swap">
<style>
:root{
  --navy:#17396b;
  --navy-dark:#112c55;
  --blue:#1d5499;
  --green:#4a9a3d;
  --green-light:#6fbb5f;
  --green-btn:#4d9c3e;
  --grey-hero-top:#e4e4e4;
  --grey-hero-bot:#c9c9c9;
  --grey-about:#efefef;
  --text:#555;
  --text-soft:#777;
  --white:#fff;
  --footer-top:#2b2b2b;
  --footer-bot:#151515;
  --footer-text:#7d7d7d;
  --border:#cfcfcf;
}
*{margin:0;padding:0;box-sizing:border-box}
html,body{width:1200px;height:2643px;overflow:hidden}
body{font-family:"Roboto",Arial,sans-serif;color:var(--text);background:var(--white);position:relative}
.abs{position:absolute}

/* header */
.site-header{position:absolute;left:0;top:0;width:1200px;height:134px}
.top-bar{position:absolute;left:0;top:0;width:1200px;height:78px;background:var(--white)}
.login-btn{position:absolute;top:10px;height:17px;padding:0 8px;font-size:10px;font-weight:700;color:var(--white);line-height:17px;letter-spacing:.3px}
.login-btn.affiliate{left:810px;background:var(--navy)}
.login-btn.merchant{left:915px;background:var(--green-btn)}
.top-links{position:absolute;top:45px;right:182px;display:flex;gap:24px;font-size:12px;font-weight:500;color:#444;letter-spacing:.2px}
.main-nav{position:absolute;left:0;top:78px;width:1200px;height:56px;background:var(--navy)}
.main-nav ul{list-style:none;position:absolute;left:480px;top:16px;display:flex;gap:30px}
.main-nav li{color:var(--white);font-size:12.5px;font-weight:700;line-height:1}
.main-nav li span{display:block;font-size:8.5px;font-weight:400;margin-top:2px;opacity:.85}
.brand{position:absolute;left:170px;top:0;width:285px;height:134px;background:var(--white);display:flex;align-items:center;justify-content:center;gap:10px;padding-top:46px}
.brand-dot{width:22px;height:22px;border-radius:50%;background:var(--green)}
.brand-name{font-size:22px;font-weight:700;color:var(--navy)}

/* hero */
.hero{position:absolute;left:0;top:134px;width:1200px;height:328px;background:linear-gradient(var(--grey-hero-top),var(--grey-hero-bot))}
.signup-btn{position:absolute;top:91px;height:30px;width:137px;font-size:13px;color:var(--white);text-align:center;line-height:30px;border:1px solid rgba(0,0,0,.15)}
.signup-btn.aff{left:183px;background:var(--green-btn)}
.signup-btn.mer{left:327px;background:var(--navy)}
.hero-title{position:absolute;left:182px;top:141px;font-size:41px;font-weight:300;line-height:40px;color:var(--white);text-shadow:0 1px 2px rgba(0,0,0,.15)}
.cta{position:absolute;left:183px;top:249px;width:137px;height:31px;background:var(--green-btn);color:var(--white);font-size:12px;text-align:center;line-height:31px}
.hero-art{position:absolute;left:540px;top:18px;width:470px;height:310px;border-radius:6px;background:linear-gradient(160deg,#1c4a86 0%,#2b5f9e 35%,#e96d57 70%,#2e3f5c 100%);opacity:.85}

/* about */
.about{position:absolute;left:0;top:462px;width:1200px;height:330px;background:var(--grey-about)}
.section-title{position:absolute;left:0;width:1200px;text-align:center;font-weight:300}
.about .section-title{top:14px;font-size:34px;color:#555}
.about-col{position:absolute;top:70px;width:400px;font-size:9.6px;line-height:17px;color:var(--text-soft);text-align:justify}
.about-col p{margin-bottom:17px}
.about-col.left{left:183px}
.about-col.right{left:600px}
.notch{position:absolute;left:565px;width:0;height:0;border-left:40px solid transparent;border-right:40px solid transparent;border-top:36px solid}

/* how it works */
.how{position:absolute;left:0;top:792px;width:1200px;height:795px;background:radial-gradient(circle at 50% 54%,#9fd08c 0%,var(--green-light) 30%,var(--green) 68%)}
.how .section-title{top:68px;font-size:33px;color:var(--white)}
.how svg{position:absolute;left:0;top:0}
.node-label{position:absolute;color:var(--white);font-size:16px;font-weight:700;line-height:17px}
.node-label span{display:block;font-weight:300}
.node-label.right-aligned{text-align:right}

/* merchants */
.merchants{position:absolute;left:0;top:1587px;width:1200px;height:378px;background:var(--white)}
.merchants .section-title{top:52px;font-size:33px;color:#555}
.merchant-box{position:absolute;width:186px;height:88px;border:1px solid var(--border);display:flex;align-items:center;justify-content:center;font-size:20px;font-weight:700}

/* testimonials */
.testimonials{position:absolute;left:0;top:1965px;width:1200px;height:390px;background:var(--blue)}
.testimonials .section-title{top:71px;font-size:33px;color:var(--white)}
.quote{position:absolute;left:215px;top:151px;width:770px;text-align:center;font-size:15px;font-style:italic;line-height:25px;color:var(--white)}
.quote-author{position:absolute;left:0;top:280px;width:1200px;text-align:center;color:var(--white);font-size:15px;letter-spacing:.5px}
.slider-dots{position:absolute;left:566px;top:333px;display:flex;gap:8px}
.slider-dots i{display:block;width:14px;height:14px;border-radius:50%;background:var(--white)}
.slider-dots i.active{background:#c7d4e6;border:3px solid var(--white)}

/* footer */
.site-footer{position:absolute;left:0;top:2355px;width:1200px;height:288px;background:linear-gradient(var(--footer-top),var(--footer-bot))}
.footer-col{position:absolute;top:54px}
.footer-col h4{font-size:15px;font-weight:400;color:var(--white);margin-bottom:16px}
.footer-col li{list-style:none;font-size:11px;color:var(--footer-text);line-height:19px;display:flex;align-items:center;gap:6px}
.social-sq{width:8px;height:8px;background:#5a78b0}
.store-badge{width:88px;height:26px;border-radius:4px;background:#4a4a4a;border:1px solid #888;margin-top:6px}
.footer-rule{position:absolute;left:183px;top:242px;width:835px;height:1px;background:#333}
.copyright{position:absolute;left:183px;top:256px;font-size:9.5px;color:#666}
</style>
</head>
<body>

<header class="site-header">
  <div class="top-bar">
    <div class="login-btn affiliate">AFFILIATE LOGIN</div>
    <div class="login-btn merchant">MERCHANT LOGIN</div>
    <nav class="top-links"><span>WHAT IS AFFILIATE MARKETING?</span><span>MERCHANTS JOIN HERE</span><span>AFFILIATE SIGN UP</span></nav>
  </div>
  <nav class="main-nav">
    <ul>
      <li>POPULAR<span>Merchants</span></li>
      <li>HOME&amp;GARDEN<span>Merchants</span></li>
      <li>FASHION<span>Merchants</span></li>
      <li>GREEN<span>Merchants</span></li>
      <li>BUSINESS<span>Merchants</span></li>
      <li>MORE<span>Merchants</span></li>
    </ul>
  </nav>
  <div class="brand"><span class="brand-dot"></span><span class="brand-name">Bluvend Market</span></div>
</header>

<section class="hero">
  <div class="signup-btn aff">Affiliates Signup</div>
  <div class="signup-btn mer">Merchants Signup</div>
  <h1 class="hero-title">Make Money<br>Make Sense.</h1>
  <div class="cta">GET STARTED</div>
  <div class="hero-art" role="img" aria-label="Illustration of an affiliate at a desk working on a computer, with speech bubbles showing sale tag, shopping basket, revenue chart and payment card, and a desk lamp"></div>
</section>

<section class="about">
  <h2 class="section-title">About Bluvend Market.</h2>
  <div class="about-col left">
    <p>Bluvend Market connects natural product makers with the people who talk about them every day. Our partners share products through blogs, social feeds, email lists and direct conversations, and every sale they drive is tracked and paid. Merchants gain a trusted sales force without upfront cost, and affiliates earn steady commission for recommending goods they already believe in. The platform handles links, reports and payouts so both sides can focus on growth.</p>
    <p>Affiliates join for free, pick the programs that match their audience and start sharing within minutes. Clear dashboards show clicks, sales and earnings in real time.</p>
    <p>Honest products, honest promotion, fair rewards.</p>
  </div>
  <div class="about-col right">
    <p>Merchants list their catalogue once and reach hundreds of motivated sales reps, bloggers and social marketers. You set the commission, approve partners and choose which creatives they may use. Every program can be searched by category, so the right affiliates find you quickly. Built on a proven partner network engine, Bluvend Market keeps tracking accurate and payments on schedule, month after month.</p>
    <p>Whether you make herbal teas, skin care or whole foods, our community helps your story travel further. Start with a free merchant account and launch your first program today with guided setup and friendly support from our team.</p>
  </div>
</section>

<section class="how">
  <svg width="1200" height="795" viewBox="0 0 1200 795">
    <g stroke="#fff" stroke-width="4" stroke-dasharray="9 6" fill="none">
      <line x1="505" y1="275" x2="550" y2="345"/>
      <line x1="695" y1="275" x2="650" y2="345"/>
      <line x1="410" y1="432" x2="485" y2="432"/>
      <line x1="720" y1="432" x2="790" y2="432"/>
      <line x1="505" y1="590" x2="550" y2="520"/>
      <line x1="695" y1="590" x2="650" y2="520"/>
    </g>
    <g fill="#fff">
      <circle cx="460" cy="219" r="71"/>
      <circle cx="740" cy="219" r="71"/>
      <circle cx="316" cy="432" r="71"/>
      <circle cx="880" cy="432" r="71"/>
      <circle cx="460" cy="654" r="71"/>
      <circle cx="740" cy="654" r="71"/>
      <circle cx="605" cy="432" r="108"/>
    </g>
    <g fill="#2a5aa0">
      <circle cx="460" cy="219" r="50" role="img" aria-label="Illustrated person representing social media promotion"/>
      <circle cx="740" cy="219" r="50" role="img" aria-label="Illustrated person representing phone calls"/>
      <circle cx="316" cy="432" r="50" role="img" aria-label="Illustrated person representing blogging"/>
      <circle cx="880" cy="432" r="50" role="img" aria-label="Illustrated person representing text messages"/>
      <circle cx="460" cy="654" r="50" role="img" aria-label="Illustrated person representing banners and apps"/>
      <circle cx="740" cy="654" r="50" role="img" aria-label="Illustrated person representing emails"/>
      <circle cx="605" cy="432" r="88" fill="#1d4a8a" role="img" aria-label="Central illustration of a sales representative surrounded by communication icons above a group of customers"/>
    </g>
  </svg>
  <h2 class="section-title">How it Works</h2>
  <div class="node-label right-aligned" style="left:300px;top:202px">Social<span>Number</span></div>
  <div class="node-label" style="left:822px;top:202px">Phone<span>Calls</span></div>
  <div class="node-label" style="left:193px;top:424px">Blog</div>
  <div class="node-label" style="left:968px;top:424px">Text<span>Message</span></div>
  <div class="node-label right-aligned" style="left:314px;top:646px">Banner<span>Apps</span></div>
  <div class="node-label" style="left:822px;top:654px">Emails</div>
</section>
<div class="notch" style="top:792px;border-top-color:var(--grey-about)"></div>

<section class="merchants">
  <h2 class="section-title">Merchants With Us</h2>
  <div class="merchant-box" style="left:183px;top:130px;color:#222">Gatepass</div>
  <div class="merchant-box" style="left:400px;top:130px;color:#2a6ab5">Vyro</div>
  <div class="merchant-box" style="left:616px;top:130px;color:#d9262a">Kelvano</div>
  <div class="merchant-box" style="left:833px;top:130px;color:#d9a100">Toyvale</div>
  <div class="merchant-box" style="left:183px;top:247px;color:#444">Marlow Trips</div>
  <div class="merchant-box" style="left:400px;top:247px;color:#1c3d7a">Casallo Hotels</div>
  <div class="merchant-box" style="left:616px;top:247px;color:#111">Ornix</div>
  <div class="merchant-box" style="left:833px;top:247px;color:#6db33f">Qelt</div>
</section>
<div class="notch" style="top:1587px;border-top-color:var(--green)"></div>

<section class="testimonials">
  <h2 class="section-title">Happy Customers</h2>
  <svg class="abs" style="left:162px;top:172px" width="22" height="48" viewBox="0 0 22 48"><polyline points="20,2 3,24 20,46" fill="none" stroke="#fff" stroke-width="2"/></svg>
  <svg class="abs" style="left:1018px;top:172px" width="22" height="48" viewBox="0 0 22 48"><polyline points="2,2 19,24 2,46" fill="none" stroke="#fff" stroke-width="2"/></svg>
  <p class="quote">At Lumbreva Stays our product availability changes frequently and we need to know that our data is of the highest possible quality. Since working with Feedrova we have noticed a significant improvement in our product data – our products are now much more visible online in the various channels. We have also been very impressed with the dedication and efficiency of the Account Management team and their ability to resolve issues so quickly.</p>
  <div class="quote-author">Alina R, Leeds</div>
  <div class="slider-dots"><i></i><i class="active"></i><i></i></div>
</section>
<div class="notch" style="top:1965px;border-top-color:var(--white)"></div>

<footer class="site-footer">
  <div class="footer-col" style="left:183px"><h4>About us</h4><ul><li>Company</li><li>Contact us</li><li>Privacy Policy</li></ul></div>
  <div class="footer-col" style="left:352px"><h4>Affiliates</h4><ul><li>Affiliates information</li><li>Affiliates link formats</li></ul></div>
  <div class="footer-col" style="left:526px"><h4>Merchants</h4><ul><li>Merchants Login</li><li>Integration methods</li><li>API Reference</li><li>Samples and Tests</li><li>Partnerly Pro</li></ul></div>
  <div class="footer-col" style="left:694px"><h4>Social</h4><ul><li><span class="social-sq"></span>Friendlane</li><li><span class="social-sq" style="background:#4aa3d8"></span>Chirpline</li><li><span class="social-sq" style="background:#c8453a"></span>Circlora</li></ul></div>
  <div class="footer-col" style="left:868px"><h4>Mobile</h4><ul><li>Get Sale Alerts</li></ul><div class="store-badge"></div><div class="store-badge"></div></div>
  <div class="footer-rule"></div>
  <div class="copyright">2014 bluvendmarket.com - All Rights Reserved</div>
</footer>

</body>
</html>
```